Business Cards and Stationery Set
Curavend Healthcare
Professional
Teodor Lisk, MD
Managing Partner
4318 West Birch Lane, Suite 207-3
Fresno, CA 93520 USA
tlisk@curavendcare.example
www.curavendcare.example

```html
<!DOCTYPE html>
<html lang="en">
<head>
<meta charset="utf-8">
<title>Curavend Healthcare — Stationery Set</title>
<link rel="stylesheet" href="https://fonts.googleapis.com/css2?family=Open+Sans:wght@400;600;700;800&display=swap">
<style>
  :root {
    --stage: #3a3c3f;
    --paper: #ffffff;
    --brand-red: #c4161c;
    --brand-deep: #7d0b10;
    --ink: #2b2b2b;
    --muted: #6f6f6f;
    --rule: #d6d6d6;
  }
  * { box-sizing: border-box; margin: 0; padding: 0; }
  html, body { width: 1200px; height: 799px; overflow: hidden; }
  body {
    background: var(--stage);
    font-family: "Open Sans", Arial, sans-serif;
    color: var(--ink);
    position: relative;
  }

  .brand { display: flex; align-items: center; gap: 7px; }
  .brand-dot { border-radius: 50%; background: var(--brand-red); flex: none; }
  .brand-name { font-weight: 800; color: var(--ink); line-height: 1.05; letter-spacing: -0.2px; }

  /* Letterhead */
  .letterhead {
    position: absolute; left: 29px; top: 60px; width: 480px; height: 696px;
    background: var(--paper); box-shadow: 0 4px 14px rgba(0,0,0,.45);
  }
  .letterhead .brand { position: absolute; left: 36px; top: 28px; }
  .letterhead .brand-dot { width: 38px; height: 38px; }
  .letterhead .brand-name { font-size: 16px; }
  .letterhead-sender {
    position: absolute; left: 318px; top: 32px;
    font-size: 6.5px; line-height: 1.5; color: var(--muted);
    border-left: 1px solid var(--rule); padding-left: 8px;
  }
  .letter-body {
    position: absolute; left: 36px; top: 112px; width: 400px;
    font-size: 7.4px; line-height: 1.5; color: #555;
  }
  .recipient { margin-bottom: 22px; }
  .salutation { margin-bottom: 12px; }
  .letter-body p { margin-bottom: 12px; }
  .closing { margin-top: 70px; }
  .signature-area {
    width: 70px; height: 20px; margin: 6px 0 4px;
    background: linear-gradient(90deg, rgba(40,60,120,.25), rgba(40,60,120,.05));
    border-radius: 3px;
  }
  .letterhead-footer {
    position: absolute; left: 0; right: 0; bottom: 0; height: 28px;
    background: linear-gradient(180deg, var(--brand-red), var(--brand-deep));
    border-top: 3px solid #e6e6e6;
    color: #fff; font-size: 7.5px; font-weight: 600; letter-spacing: 1.2px;
    display: flex; align-items: center; justify-content: center;
  }

  /* Business card */
  .business-card {
    position: absolute; left: 677px; top: 53px; width: 499px; height: 271px;
    background: var(--paper); box-shadow: 0 4px 14px rgba(0,0,0,.45);
  }
  .business-card .brand { position: absolute; left: 34px; top: 88px; }
  .business-card .brand-dot { width: 52px; height: 52px; }
  .business-card .brand-name { font-size: 24px; }
  .card-details { position: absolute; left: 250px; top: 36px; width: 220px; }
  .card-name { color: var(--brand-red); font-size: 15px; font-weight: 700; }
  .card-role { font-size: 9px; color: var(--muted); margin-top: 2px; }
  .card-rule { height: 1px; background: var(--rule); margin: 12px 0 10px; }
  .card-address { font-size: 8.5px; line-height: 1.5; color: #555; margin-bottom: 10px; }
  .contact-line { display: flex; align-items: center; gap: 6px; font-size: 8.5px; color: #555; margin-bottom: 5px; }
  .contact-line svg { width: 9px; height: 9px; flex: none; }
  .card-footer {
    position: absolute; left: 0; right: 0; bottom: 0; height: 36px;
    background: linear-gradient(180deg, var(--brand-red), var(--brand-deep));
    border-top: 3px solid #e6e6e6;
    color: #fff; font-size: 10px; font-weight: 600; letter-spacing: 1.6px;
    display: flex; align-items: center; justify-content: center;
  }

  /* Envelope back */
  .envelope-back {
    position: absolute; left: 598px; top: 360px; width: 578px; height: 215px;
    box-shadow: 0 4px 14px rgba(0,0,0,.45);
  }
  .envelope-back svg { display: block; }
  .envelope-back .brand-dot {
    position: absolute; left: 267px; top: 104px; width: 44px; height: 44px;
  }

  /* Envelope front */
  .envelope-front {
    position: absolute; left: 598px; top: 588px; width: 578px; height: 202px;
    background: var(--paper); box-shadow: 0 4px 14px rgba(0,0,0,.45);
  }
  .envelope-front .brand { position: absolute; left: 34px; top: 34px; }
  .envelope-front .brand-dot { width: 40px; height: 40px; }
  .envelope-front .brand-name { font-size: 18px; }
  .envelope-return { position: absolute; left: 34px; top: 86px; font-size: 7px; line-height: 1.5; color: var(--muted); }
  .envelope-footer {
    position: absolute; left: 0; right: 0; bottom: 0; height: 22px;
    background: linear-gradient(180deg, var(--brand-red), var(--brand-deep));
    border-top: 3px solid #e6e6e6;
    color: #fff; font-size: 7.5px; font-weight: 600; letter-spacing: 1.2px;
    display: flex; align-items: center; justify-content: center;
  }
</style>
</head>
<body>

<section class="letterhead">
  <div class="brand"><span class="brand-dot"></span><span class="brand-name">Curavend<br>Healthcare</span></div>
  <div class="letterhead-sender">
    4318 West Birch Lane, Suite 207-3<br>
    Fresno, CA 93520 USA<br>
    +1 (559) 555-0142
  </div>
  <div class="letter-body">
    <div class="recipient">Someone Name here<br>1000 Long St,<br>Brisbane, Australia</div>
    <div class="salutation">Dear Someone Something,</div>
    <p>Thank you for your recent visit to our clinic. We are pleased to confirm that your care plan has been reviewed by our team and approved for the coming quarter. Our staff will contact you shortly to arrange follow-up appointments at a time that suits you best.</p>
    <p>Please bring any recent test results and a list of current medications to your next visit. If you have questions before then, our patient services desk is available on weekdays and will gladly help with scheduling, billing or referrals.</p>
    <p>We value the trust you place in our practice and look forward to supporting your health in the months ahead.</p>
    <div class="closing">Yours Sincerely,<br>Marten Holloway</div>
    <div class="signature-area" role="img" aria-label="Handwritten signature"></div>
  </div>
  <div class="letterhead-footer">www.curavendcare.example</div>
</section>

<section class="business-card">
  <div class="brand"><span class="brand-dot"></span><span class="brand-name">Curavend</span></div>
  <div class="card-details">
    <div class="card-name">Teodor Lisk, MD</div>
    <div class="card-role">Managing Partner</div>
    <div class="card-rule"></div>
    <div class="card-address">4318 West Birch Lane, Suite 207-3<br>Fresno, CA 93520 USA</div>
    <div class="contact-line">
      <svg viewBox="0 0 10 10"><path d="M2 1h2l1 2.5-1.3 1a5 5 0 0 0 2 2l1-1.3L9 6v2a1 1 0 0 1-1 1A7 7 0 0 1 1 2a1 1 0 0 1 1-1z" fill="#c4161c"/></svg>
      +1 (559) 555-0142
    </div>
    <div class="contact-line">
      <svg viewBox="0 0 10 10"><rect x="1" y="3" width="8" height="5" rx="1" fill="#c4161c"/><rect x="3" y="1" width="4" height="2.5" fill="#c4161c"/></svg>
      +1 (559) 555-0187
    </div>
    <div class="contact-line">
      <svg viewBox="0 0 10 10"><rect x="1" y="2" width="8" height="6" rx="1" fill="#c4161c"/><path d="M1.5 2.5 5 5.5l3.5-3" stroke="#fff" fill="none" stroke-width=".8"/></svg>
      tlisk@curavendcare.example
    </div>
  </div>
  <div class="card-footer">www.curavendcare.example</div>
</section>

<section class="envelope-back">
  <svg width="578" height="215" viewBox="0 0 578 215">
    <defs>
      <linearGradient id="flapInside" x1="0" y1="0" x2="0" y2="1">
        <stop offset="0" stop-color="#5f070b"/>
        <stop offset="1" stop-color="#c4161c"/>
      </linearGradient>
    </defs>
    <rect width="578" height="215" fill="url(#flapInside)"/>
    <polygon points="0,52 289,150 578,52 578,215 0,215" fill="#ffffff"/>
    <polyline points="0,52 289,150 578,52" fill="none" stroke="#d9d9d9" stroke-width="1"/>
    <line x1="0" y1="215" x2="250" y2="140" stroke="#e2e2e2"/>
    <line x1="578" y1="215" x2="328" y2="140" stroke="#e2e2e2"/>
  </svg>
  <span class="brand-dot"></span>
</section>

<section class="envelope-front">
  <div class="brand"><span class="brand-dot"></span><span class="brand-name">Curavend Healthcare</span></div>
  <div class="envelope-return">4318 West Birch Lane, Suite 207-3<br>Fresno, CA 93520 USA</div>
  <div class="envelope-footer">www.curavendcare.example</div>
</section>

</body>
</html>
```